Brackwell Removals

We are a domestic removals company, providing the following service:
- removals service
- packing service
- packing materials
- storage facility
- furniture dismantling and reassembling
We would like to start a flyer campaign to customers that just agreed for the house sale.
Our strong key points:
- Good Reviews (Revuemark, Zentrix, shiftquote.com and pagebook)
- Two Men Service (we do all the heavy work for the customer, and place the furniture and boxes to each room of destination)
- Fully Insured
- We can take bookings 7-days of week
- Free and no-obligation survey (we need to do a house visit first in order to provide a fixed and accurate quote)
- Free Quote
Technical Specs:
Landline number: 01632 960418
Contact email: office@brackwellremovals.example.co.uk
Address: Unit 14, Carrow Lane, Northampton NN9 4QT
Website: brackwellremovals.example.co.uk
Took a look on the onto previous projects on FX.com, and liked several flyers already done by you guys, for this industry
We'd like to integrate the colours from our logo in the flyer as well !!

```html
<!DOCTYPE html>
<html lang="en">
<head>
<meta charset="utf-8">
<title>Brackwell Removals – Flyer</title>
<link rel="stylesheet" href="https://fonts.googleapis.com/css2?family=Roboto+Condensed:wght@700;800&family=Arimo:wght@400&display=swap">
<style>
  :root {
    --red: #cc3a12;
    --teal: #18798a;
    --navy: #123a66;
    --white: #ffffff;
    --orange: #f59a2c;
    --stage: #5fadde;
  }
  * { box-sizing: border-box; margin: 0; padding: 0; }
  html, body { width: 1200px; height: 900px; overflow: hidden; }
  body { background: var(--stage); position: relative; font-family: "Arimo", Arial, sans-serif; }

  .flyer {
    position: absolute; left: 290px; top: 15px;
    width: 621px; height: 870px;
    background: var(--white); overflow: hidden;
    box-shadow: 0 12px 30px rgba(0,0,0,.25);
  }
  .flyer-shapes { position: absolute; inset: 0; width: 100%; height: 100%; }
  .flyer > *:not(.flyer-shapes) { position: absolute; }

  .mascot-art {
    left: 6px; top: 14px; width: 236px; height: 150px;
    background: linear-gradient(160deg, #f7a83c 0%, #f28a1f 55%, #1b7487 100%);
    border-radius: 4px;
  }
  .brand-name {
    left: 16px; top: 170px;
    font-family: "Roboto Condensed", Arial, sans-serif; font-weight: 800;
    color: var(--teal); font-size: 40px; line-height: 40px; text-transform: uppercase;
  }

  .hero-claim {
    right: 19px; top: 26px; text-align: right;
    font-family: "Roboto Condensed", Arial, sans-serif; font-weight: 800;
    color: var(--white); text-transform: uppercase; line-height: 1.02;
  }
  .hero-claim span { display: block; }
  .hero-claim .s1 { font-size: 36px; }
  .hero-claim .s2 { font-size: 46px; }
  .hero-claim .s3 { font-size: 60px; }
  .hero-claim .s4 { font-size: 48px; }

  .intro {
    left: 23px; top: 280px; width: 580px;
    font-family: "Roboto Condensed", Arial, sans-serif; font-weight: 700;
    color: var(--white); font-size: 46px; line-height: 55px;
  }

  .services {
    left: 352px; top: 409px; list-style: none;
    color: var(--white); font-size: 18px; line-height: 22px;
  }
  .services li { padding-left: 17px; position: relative; }
  .services li::before {
    content: ""; position: absolute; left: 1px; top: 7px;
    width: 7px; height: 7px; border: 1.3px solid var(--white); border-radius: 50%;
  }

  .key-title {
    left: 31px; top: 462px;
    font-family: "Roboto Condensed", Arial, sans-serif; font-weight: 800;
    color: var(--white); font-size: 48px; line-height: 51px;
  }

  .key-points {
    left: 19px; top: 591px; width: 580px; list-style: none;
    color: var(--white); font-size: 15.5px; line-height: 20px;
  }
  .key-points li { padding-left: 20px; position: relative; }
  .key-points li svg { position: absolute; left: 0; top: 7px; width: 9px; height: 8px; }

  .contact { color: var(--white); font-size: 12px; line-height: 14px; }
  .contact svg { position: absolute; left: 0; }
  .address { left: 22px; top: 786px; padding-left: 25px; }
  .address svg { top: 1px; width: 14px; height: 20px; }
  .phone {
    left: 197px; top: 790px; padding-left: 23px;
    font-family: "Roboto Condensed", Arial, sans-serif; font-weight: 700; font-size: 18px; line-height: 20px;
  }
  .phone svg { top: 2px; width: 16px; height: 16px; }
  .web { left: 22px; top: 822px; padding-left: 25px; }
  .email { left: 22px; top: 837px; padding-left: 25px; }
  .web svg, .email svg { top: 1px; width: 13px; height: 12px; }

  .footer-mark {
    left: 402px; top: 785px; width: 82px; height: 82px;
    border-radius: 50%; background: var(--orange); border: 5px solid #1f2e3a;
  }
  .footer-name {
    left: 492px; top: 800px;
    font-family: "Roboto Condensed", Arial, sans-serif; font-weight: 800;
    color: var(--teal); font-size: 23px; line-height: 24px; text-transform: uppercase;
  }
</style>
</head>
<body>
<main class="flyer">
  <svg class="flyer-shapes" viewBox="0 0 621 870" preserveAspectRatio="none" aria-hidden="true">
    <polygon points="274,0 621,0 621,272 240,272" fill="var(--red)"/>
    <rect x="0" y="271" width="621" height="295" fill="var(--teal)"/>
    <rect x="0" y="561" width="621" height="207" fill="var(--navy)"/>
    <polygon points="0,453 288,453 329,578 0,578" fill="var(--red)"/>
    <rect x="0" y="767" width="621" height="103" fill="var(--teal)"/>
    <polygon points="335,776 621,773 621,870 395,870" fill="var(--white)"/>
  </svg>

  <div class="mascot-art" role="img" aria-label="Illustration of a smiling removals worker in a teal polo shirt in front of an orange house"></div>
  <p class="brand-name">Brackwell<br>Removals</p>

  <h1 class="hero-claim">
    <span class="s1">We are specialised</span>
    <span class="s1">in making your</span>
    <span class="s2">move run as</span>
    <span class="s3">smoothly</span>
    <span class="s4">as possible</span>
  </h1>

  <p class="intro">We are a domestic removals company, providing the following service:</p>

  <ul class="services">
    <li>removals service</li>
    <li>packing service</li>
    <li>packing materials</li>
    <li>storage facility</li>
    <li>furniture dismantling<br>and reassembling</li>
  </ul>

  <h2 class="key-title">Our strong<br>&nbsp;key points:</h2>

  <ul class="key-points">
    <li><svg viewBox="0 0 9 8"><path d="M1 4.2 3.4 6.6 8 1.2" fill="none" stroke="#fff" stroke-width="1.8"/></svg>Good Reviews (Revuemark, Zentrix, shiftquote.com and pagebook)</li>
    <li><svg viewBox="0 0 9 8"><path d="M1 4.2 3.4 6.6 8 1.2" fill="none" stroke="#fff" stroke-width="1.8"/></svg>Two Men Service (we do all the heavy work for the customer, and place the furniture and boxes to each room of destination)</li>
    <li><svg viewBox="0 0 9 8"><path d="M1 4.2 3.4 6.6 8 1.2" fill="none" stroke="#fff" stroke-width="1.8"/></svg>Fully Insured</li>
    <li><svg viewBox="0 0 9 8"><path d="M1 4.2 3.4 6.6 8 1.2" fill="none" stroke="#fff" stroke-width="1.8"/></svg>We can take bookings 7-days of week</li>
    <li><svg viewBox="0 0 9 8"><path d="M1 4.2 3.4 6.6 8 1.2" fill="none" stroke="#fff" stroke-width="1.8"/></svg>Free and no-obligation survey (we need to do a house visit first in order to provide a fixed and accurate quote)</li>
    <li><svg viewBox="0 0 9 8"><path d="M1 4.2 3.4 6.6 8 1.2" fill="none" stroke="#fff" stroke-width="1.8"/></svg>Free Quote</li>
  </ul>

  <p class="contact address">
    <svg viewBox="0 0 14 20"><path d="M7 1a6 6 0 0 0-6 6c0 4.5 6 12 6 12s6-7.5 6-12a6 6 0 0 0-6-6z" fill="none" stroke="#fff" stroke-width="1.6"/><circle cx="7" cy="7" r="2.2" fill="#fff"/></svg>
    Unit 14, Carrow Lane,<br>Northampton NN9 4QT
  </p>
  <p class="contact phone">
    <svg viewBox="0 0 16 16"><rect x="0.5" y="0.5" width="15" height="15" rx="3" fill="#fff"/><path d="M5 3.5 6.6 5.8 5.6 7c.7 1.5 1.8 2.6 3.3 3.3l1.2-1 2.3 1.6-.9 1.8C8 12.5 3.6 8.1 3.3 4.4z" fill="var(--teal)"/></svg>
    01632 960418
  </p>
  <p class="contact web">
    <svg viewBox="0 0 13 12"><circle cx="6.5" cy="6" r="5.3" fill="none" stroke="#fff"/><ellipse cx="6.5" cy="6" rx="2.4" ry="5.3" fill="none" stroke="#fff"/><path d="M1.2 6h10.6M2 3.3h9M2 8.7h9" stroke="#fff" stroke-width=".8"/></svg>
    brackwellremovals.example.co.uk
  </p>
  <p class="contact email">
    <svg viewBox="0 0 13 12"><rect x=".5" y="2" width="12" height="8.5" fill="none" stroke="#fff"/><path d="M.5 2 6.5 7l6-5" fill="none" stroke="#fff"/></svg>
    office@brackwellremovals.example.co.uk
  </p>

  <div class="footer-mark" aria-hidden="true"></div>
  <p class="footer-name">Brackwell<br>Removals</p>
</main>
</body>
</html>
```